Task Description:
I’m wanting a professionally designed 8 ½' x 11, 3 fold brochure, both sides, to print as my target audience are those people who primarily don’t have access to the internet. These items will be dropped off in the mailboxes of all households in the city.
However I do have a web site www.brightcivicpath.ca where I would like to have it as a document that can be down loaded.
This is my first foray into political office and my message needs to be clear, concise and easy to understand. The brochure should be a bit conservative yet be warm and inviting. I’ve selected two pictures that I think make sense under their respective headings, but I'm open to suggestions.I need to update my picture for the front cover.
There is the possibility of having T shirts and business cards made up, which would be in essence a simpler version of the brochure so please keep this in mind. I ask that you work with me and I will compensate you accordingly for the extras should they be required. You may want to consider making the Bright Civic Path into a logo as we own all the web extensions and have applied for copyright protection for branding purposes.
You may want to look at QM Larchfield http://www.qmlarchfield.ca/ , or the Pinecrest Bank of Canada www.pinecrestbank.com as two recognizable colour schemes here in Canada but don’t let that limit your imagination.
The content in the flier should remain intact although I am open to some minor suggestions. As you can see my talents as a graphic artist are limited hence my need for that professional make over that will give it a bit of razzle dazzle and set me out from the other candidates. So use your imagination!!
Target Market(s)
Middle age voters who may or may not have access to the internet and still prefer print
Industry/Entity Type
Conservative

```html
<!DOCTYPE html>
<html lang="en">
<head>
<meta charset="utf-8">
<title>Bright Civic Path – Brochure Inside</title>
<link rel="stylesheet" href="https://fonts.googleapis.com/css2?family=Questrial&display=swap">
<style>
  :root {
    --band-red: #c8202a;
    --sky-light: #a9dcf0;
    --sky-mid: #5fc3e6;
    --sky-deep: #3fb3de;
    --rule-navy: #2a3f8f;
    --ink: #2b2b2b;
    --heading-ink: #1f1f1f;
  }
  html, body {
    margin: 0;
    padding: 0;
    overflow: hidden;
    background: #ffffff;
  }
  .brochure-panel {
    position: relative;
    width: 927px;
    height: 1200px;
    overflow: hidden;
    font-family: "Questrial", "Century Gothic", sans-serif;
    color: var(--ink);
    background: radial-gradient(ellipse at 50% 12%, var(--sky-light) 0%, var(--sky-mid) 55%, var(--sky-deep) 100%);
  }
  .band {
    position: absolute;
    left: 0;
    width: 100%;
    background: var(--band-red);
  }
  .band--top { top: 0; height: 24px; }
  .band--bottom { bottom: 0; height: 29px; }

  .column-rule {
    position: absolute;
    top: 37px;
    height: 1113px;
    width: 1px;
    background: var(--rule-navy);
  }
  .column-rule--one { left: 309px; }
  .column-rule--two { left: 619px; }

  .column {
    position: absolute;
    top: 172px;
  }
  .column--economy { left: 32px; width: 268px; }
  .column--opportunity { left: 328px; width: 269px; }
  .column--safety { left: 627px; width: 257px; }

  .column-heading {
    margin: 0 0 27px;
    font-weight: 400;
    font-size: 23px;
    line-height: 38px;
    text-align: center;
    color: var(--heading-ink);
    text-transform: uppercase;
    letter-spacing: 0.2px;
  }
  .column--opportunity .column-heading { margin-bottom: 22px; }

  .column p {
    margin: 0;
    font-size: 14.4px;
    line-height: 20.7px;
    text-align: justify;
    hyphens: manual;
  }
  .column .lead-paragraph::first-letter { font-size: 19px; }

  .column--economy p { margin-bottom: 45px; }
  .column--economy p.paragraph--tight { margin-bottom: 23px; }

  .column--opportunity p { line-height: 21.3px; margin-bottom: 20px; }

  .column--safety p { margin-bottom: 43px; }

  .photo-family {
    position: absolute;
    left: 646px;
    top: 726px;
    width: 234px;
    height: 172px;
    background: linear-gradient(160deg, #5a5d68 0%, #3b3a40 45%, #8a7f86 100%);
    box-shadow: 0 0 0 1px rgba(255,255,255,0.6);
  }
  .photo-caption {
    position: absolute;
    left: 627px;
    top: 921px;
    width: 257px;
    margin: 0;
    font-size: 13.5px;
    text-align: center;
    text-transform: uppercase;
    color: var(--heading-ink);
  }

  .site-address {
    position: absolute;
    top: 1131px;
    width: 309px;
    margin: 0;
    font-size: 14px;
    text-align: center;
    color: var(--heading-ink);
  }
  .site-address--left { left: 0; }
  .site-address--middle { left: 309px; width: 310px; }
  .site-address--right { left: 619px; }
</style>
</head>
<body>
<main class="brochure-panel">
  <div class="band band--top"></div>

  <div class="column-rule column-rule--one"></div>
  <div class="column-rule column-rule--two"></div>

  <section class="column column--economy">
    <h2 class="column-heading">A Strong Economy</h2>
    <p class="lead-paragraph">Without a strong economy we can't afford to pay for social services that we now take for granted.</p>
    <p>Although the City is the largest corpora&shy;tion it is unique in the fact that it revenue stream is tied directly to taxation</p>
    <p>Without new business and new citizens the burden of taxes will fall increasingly on residential taxpayers.</p>
    <p>Our demographics have changed over the years and those changes need to be reflected in the way we tax our citi&shy;zens.</p>
    <p class="paragraph--tight">Our levels of debts and our future com&shy;mitments need to be effectively com&shy;municated to the people that own this city. You the tax payer!!</p>
    <p>Currently our debt is 178 million dollars with further commitments of 153 million for homes for the aged and the possibil&shy;ity of 100 million dollar multi purpose fa&shy;cility. How will we pay for this?</p>
  </section>

  <section class="column column--opportunity">
    <h2 class="column-heading">New Opportunities<br>New Beginings</h2>
    <p class="lead-paragraph">As a city we need to rekindle that pas&shy;sion that made us the most modern small city in North America at the turn of the century.</p>
    <p>That means, if you currently own and operate a business large or small we need your input to improve the efficien&shy;cy of how we deliver services. No more endless meetings without any results.</p>
    <p>If you're in the planning stages and need assistance, the city will be there to offer support and guidance.</p>
    <p>Regional projects are vitality important to the flow of goods and services.</p>
    <p>As a Bright Civic Path I have personally spoken to the CEO's of several new in&shy;dustries that have never even consid&shy;ered Harbour Ridge before they received my call. These are leading edge tech&shy;nologies that have the high growth po&shy;tential. Jobs and opportunities for young and old alike.</p>
    <p>Are we open for business absolutely!</p>
  </section>

  <section class="column column--safety">
    <h2 class="column-heading">A Safe Community</h2>
    <p class="lead-paragraph">Without a safe community it will be difficult to attract new people and new businesses to our community.</p>
    <p>I have a plan that will utilize the re&shy;sources of the current police force to better facilitate the services that are currently provided.</p>
    <p>Incentive programs need to be initi&shy;ated in all city departments at the ground level so that good ideas don't get lost in bureaucracy.</p>
    <p>Seniors and youth are the most vulner&shy;able of all. I have plan that will identify those groups and make sure that those people receive the benefits that they deserve.</p>
  </section>

  <div class="photo-family" role="img" aria-label="Photo of the candidate's 92-year-old father seated in arena stands beside a team mascot"></div>
  <p class="photo-caption">My Dad @ 92 with NLU Mascot</p>

  <p class="site-address site-address--left">www.brightcivicpath.ca</p>
  <p class="site-address site-address--middle">www.brightcivicpath.ca</p>
  <p class="site-address site-address--right">www.brightcivicpath.ca</p>

  <div class="band band--bottom"></div>
</main>
</body>
</html>
```